Bright Fern Property Services

Design a billboard with our logo that includes bullet points for
Property Maintenance, Plumbing, and Electrical, licensed and insured.
Phone number 865 418 3907

also add the website brightfernps-example.com

```html
<!DOCTYPE html>
<html lang="en">
<head>
<meta charset="utf-8">
<title>Bright Fern Property Services – Billboard</title>
<link rel="stylesheet" href="https://fonts.googleapis.com/css2?family=Outfit:wght@500;600;700&display=swap">
<style>
  :root {
    --brand-green: #4faa28;
    --ink: #2a2a2a;
    --paper: #ffffff;
    --backdrop: #eef0f2;
  }
  * { margin: 0; padding: 0; box-sizing: border-box; }
  html, body {
    width: 1200px;
    height: 1114px;
    overflow: hidden;
    background: var(--backdrop);
    font-family: "Outfit", sans-serif;
  }
  .billboard {
    position: absolute;
    left: 20px;
    top: 375px;
    width: 1515px;
    height: 475px;
    background: var(--paper);
    transform: scale(0.7657);
    transform-origin: top left;
    overflow: hidden;
  }
  .billboard__shapes {
    position: absolute;
    inset: 0;
  }
  .brand-name {
    position: absolute;
    left: 58px;
    top: 108px;
    color: var(--brand-green);
    font-weight: 700;
    line-height: 1;
    white-space: nowrap;
  }
  .brand-name__main {
    display: block;
    font-size: 100px;
    letter-spacing: 1px;
    text-transform: uppercase;
  }
  .brand-name__sub {
    display: block;
    margin-top: 22px;
    font-size: 44px;
    letter-spacing: 9px;
    text-transform: uppercase;
  }
  .headline {
    position: absolute;
    right: 30px;
    top: 36px;
    font-size: 58px;
    font-weight: 700;
    color: var(--ink);
    letter-spacing: 0.5px;
    white-space: nowrap;
  }
  .service-list {
    position: absolute;
    left: 965px;
    top: 175px;
    list-style: none;
  }
  .service-list__item {
    display: flex;
    align-items: center;
    height: 108px;
    font-size: 92px;
    font-weight: 700;
    color: var(--ink);
    white-space: nowrap;
  }
  .service-list__icon {
    width: 92px;
    height: 92px;
    margin-right: 30px;
    flex: none;
  }
  .badge-text {
    position: absolute;
    right: 40px;
    top: 408px;
    font-size: 40px;
    font-weight: 600;
    color: var(--paper);
    white-space: nowrap;
  }
  .contact {
    position: absolute;
    left: 22px;
    top: 390px;
    display: flex;
    align-items: center;
    gap: 20px;
    color: var(--paper);
    font-size: 34px;
    font-weight: 600;
    font-style: normal;
    white-space: nowrap;
  }
  .contact__item {
    display: flex;
    align-items: center;
    gap: 8px;
  }
  .contact__icon {
    width: 28px;
    height: 28px;
  }
</style>
</head>
<body>
  <main class="billboard">
    <svg class="billboard__shapes" viewBox="0 0 1515 475" aria-hidden="true">
      <path fill="var(--brand-green)"
        d="M0,354 H805 C845,354 862,335 878,296 L925,178 C940,142 958,130 1000,130 H1515 V152 H1008 C978,152 964,162 952,192 L828,475 H0 Z"/>
      <path fill="var(--brand-green)"
        d="M1058,475 L1078,428 C1085,412 1095,405 1115,405 H1515 V475 Z"/>
    </svg>

    <h1 class="brand-name">
      <span class="brand-name__main">Bright Fern</span>
      <span class="brand-name__sub">Property Services</span>
    </h1>

    <p class="headline">PROPERTY MAINTENANCE</p>

    <ul class="service-list">
      <li class="service-list__item">
        <svg class="service-list__icon" viewBox="0 0 92 92" aria-hidden="true">
          <circle cx="46" cy="46" r="40" fill="none" stroke="var(--ink)" stroke-width="6"/>
          <rect x="40" y="18" width="14" height="5" fill="var(--ink)"/>
          <rect x="44" y="22" width="6" height="10" fill="var(--ink)"/>
          <path d="M18,36 H60 C68,36 72,42 72,50 V56 H62 V50 C62,47 60,46 58,46 H18 Z" fill="var(--ink)"/>
          <path d="M67,62 C70,67 72,70 72,73 C72,76 70,78 67,78 C64,78 62,76 62,73 C62,70 64,67 67,62 Z" fill="var(--ink)"/>
        </svg>
        Plumbing
      </li>
      <li class="service-list__item">
        <svg class="service-list__icon" viewBox="0 0 92 92" aria-hidden="true">
          <path d="M36,10 A40,40 0 0 0 36,82" fill="none" stroke="var(--ink)" stroke-width="6"/>
          <path d="M60,12 A40,40 0 0 1 60,80" fill="none" stroke="var(--ink)" stroke-width="6"/>
          <path d="M54,2 L24,52 H44 L38,90 L70,38 H50 Z" fill="var(--ink)"/>
        </svg>
        Electrical
      </li>
    </ul>

    <p class="badge-text">licensed and insured</p>

    <address class="contact">
      <span class="contact__item">
        <svg class="contact__icon" viewBox="0 0 24 24" aria-hidden="true">
          <path fill="var(--paper)" d="M6.6,10.8 C8,13.6 10.4,16 13.2,17.4 L15.4,15.2 C15.7,14.9 16.1,14.8 16.4,15 C17.5,15.4 18.7,15.6 20,15.6 C20.6,15.6 21,16 21,16.6 V20 C21,20.6 20.6,21 20,21 C10.6,21 3,13.4 3,4 C3,3.4 3.4,3 4,3 H7.5 C8.1,3 8.5,3.4 8.5,4 C8.5,5.3 8.7,6.5 9.1,7.6 C9.2,7.9 9.1,8.3 8.9,8.6 Z"/>
        </svg>
        865 418 3907
      </span>
      <span class="contact__item">
        <svg class="contact__icon" viewBox="0 0 24 24" aria-hidden="true">
          <g fill="none" stroke="var(--paper)" stroke-width="2">
            <circle cx="12" cy="12" r="9"/>
            <ellipse cx="12" cy="12" rx="4" ry="9"/>
            <path d="M3,12 H21 M5,7 H19 M5,17 H19"/>
          </g>
        </svg>
        brightfernps-example.com
      </span>
    </address>
  </main>
</body>
</html>
```